High-end executive coaching group needs a 2 page digital flyer

We need a 2 page digital flyer for a high end leadership coaching offering for global leaders in healthcare. The flyer will advertise a new service (an elite senior leadership coaching group) for senior leaders in the healthcare industry from around the world.
The flyer should be upmarket, professional and minimalist in style to meet the expectations of my professional market (very senior doctors and executives).
The design should be based on my existing logo and brand, see my landing page: www.lantavereadvisory.com
The key elements needed are
1) An editable PDF which we can update as we revise the specific details of the offering. The text and draft design for this is attached.
2) The banner image should be high quality but abstract. It can be based on the landing page of my website (the two ripple effects) but does not need to strictly adhere to this.
3) The logo placement of the Lantavere Advisory delta sign should be discreet so that it does not dominate
4) The small logos of our professional accrediting organisations should be discreetly placed at the end and should not dominate. They might work best as mono icons in a footer (e.g. blue on a white background, or white on blue.
5) Please find enclosed a previous flyer as an example of a similar style we have used for more junior professionals. The design worked quite well, although we now need a more upmarket version for our senior executives.
Updates

Please note this design specifically needs to use existing branding and images from my website: lantavereadvisory.com. We are definitely not looking for stock "leadership team" images for this high-end brochure.

Target Market(s)

Senior global leaders in the healthcare industry

Industry/Entity Type

Leading business schools & Healthcare industry.

Font styles to use
Other font styles liked:
• Operetta (selective use for heading) and Sofia Pro (body text)

Colors
0054AA
0677BA
7BADD7
CADEEF
E8F1F8

Requirements
Must have
• Clean minimalist and high professionally look that directly speaks to the interests and perspectives of senior leader leaders in healthcare. It also needs very clear call to action sections
Nice to have
• Effective presentation of the two bios and photographs. These need to look impressive, but should not dominate.
Should not have
• Loud and bold colours, large use of logos.

```html
<!DOCTYPE html>
<html lang="en">
<head>
<meta charset="utf-8">
<title>Elevate and Ignite Your Leadership – Lantavere Advisory</title>
<link href="https://fonts.googleapis.com/css2?family=Libre+Caslon+Text:wght@400;700&family=Mulish:wght@400;500;600&display=swap" rel="stylesheet">
<style>
  :root{
    --brand-deep:#0054aa;
    --brand-mid:#0677ba;
    --brand-navy:#1d4a9a;
    --brand-soft:#7badd7;
    --brand-pale:#cadeef;
    --brand-mist:#e8f1f8;
    --slate:#6a86ad;
    --ink:#1f2a3a;
    --white:#ffffff;
  }
  *{margin:0;padding:0;box-sizing:border-box}
  html,body{width:849px;height:1200px;overflow:hidden;background:var(--white)}
  body{font-family:"Mulish",sans-serif;color:var(--ink)}
  .flyer{position:relative;width:849px;height:1200px;overflow:hidden;
    background:linear-gradient(180deg,#eceef1 0%,#f4f5f7 45%,var(--brand-pale) 49.4%,var(--brand-pale) 100%)}
  .hero-image{position:absolute;left:0;top:0;width:849px;height:593px}
  .brand{position:absolute;left:37px;top:108px;display:flex;align-items:center;gap:12px}
  .brand-mark{width:16px;height:16px;background:var(--brand-navy)}
  .brand-name{font-family:"Libre Caslon Text",serif;font-weight:400;font-size:26px;line-height:1.05;color:var(--brand-navy);width:170px}
  .headline{position:absolute;left:39px;top:198px;font-family:"Libre Caslon Text",serif;font-weight:700;font-size:29px;line-height:1.24;color:var(--brand-navy)}
  .banner{position:absolute;left:0;top:299px;width:684px;height:63px;background:var(--brand-deep);
    clip-path:polygon(0 0,668px 0,684px 63px,0 63px);color:var(--white);padding:11px 0 0 37px;font-size:15.5px;line-height:1.3}
  .banner strong{font-weight:600;letter-spacing:.2px}
  .section-title{position:absolute;font-family:"Libre Caslon Text",serif;font-weight:400;font-size:19.5px;color:var(--brand-navy)}
  .offer-title{left:37px;top:382px}
  .benefits-title{left:37px;top:624px}
  .intro-card{position:absolute;top:419px;width:328px;height:153px;background:var(--brand-pale);border-radius:16px;
    font-size:16px;line-height:20.3px;color:var(--ink)}
  .intro-card.left{left:62px;padding:12px 46px 0 14px}
  .intro-card.right{left:460px;background:#d3e3f1;padding:12px 22px 0 12px}
  .benefits{position:absolute;left:37px;top:662px;width:332px;list-style:none;font-size:16px;line-height:20.8px}
  .benefits li{position:relative;padding-left:26px;margin-bottom:3px}
  .benefits li svg{position:absolute;left:0;top:5px}
  .quote-card{position:absolute;left:460px;top:695px;width:326px;height:259px;background:var(--white);border-radius:22px;
    padding:22px 14px 0 14px}
  .quote-card p{font-size:16.5px;line-height:21.4px;color:var(--ink)}
  .quote-card cite{display:block;text-align:right;margin-top:16px;padding-right:2px;font-family:"Libre Caslon Text",serif;font-style:normal;font-weight:700;font-size:16.5px;color:var(--brand-navy)}
  .quote-mark{position:absolute;font-family:"Libre Caslon Text",serif;font-weight:700;font-size:78px;line-height:1;color:var(--brand-navy)}
  .quote-mark.open{left:443px;top:668px}
  .quote-mark.close{left:752px;top:925px}
  .details{position:absolute;left:0;top:1042px;width:438px;height:158px;background:var(--brand-deep);
    clip-path:polygon(0 0,412px 0,438px 158px,0 158px);color:var(--white);padding:12px 0 0 37px;font-size:14.5px;line-height:18.8px}
  .details .indent{padding-left:35px}
  .cta{position:absolute;left:417px;top:1106px;width:432px;height:94px;background:var(--slate);
    clip-path:polygon(0 0,432px 0,432px 94px,16px 94px);color:var(--white);padding:18px 0 0 71px;font-size:16px;line-height:21px}
</style>
</head>
<body>
<main class="flyer">
  <svg class="hero-image" viewBox="0 0 849 593" role="img" aria-label="Aerial photograph of dark rocks and turquoise waves breaking along a rocky shoreline">
    <defs>
      <linearGradient id="seaTone" x1="0" y1="0" x2="1" y2="1">
        <stop offset="0" stop-color="#5a5450"/>
        <stop offset="0.4" stop-color="#2f4a50"/>
        <stop offset="0.7" stop-color="#1a6f78"/>
        <stop offset="1" stop-color="#123c4a"/>
      </linearGradient>
    </defs>
    <polygon points="352,0 849,0 849,593 455,593 700,362 600,300" fill="url(#seaTone)"/>
  </svg>

  <div class="brand">
    <span class="brand-mark"></span>
    <span class="brand-name">Lantavere Advisory</span>
  </div>

  <h1 class="headline">Elevate and Ignite<br>Your Leadership</h1>

  <div class="banner">
    <strong>TRANSFORMATIVE CONVERSATIONS FOR SENIOR HEALTHCARE LEADERS.</strong><br>
    Unlock purpose, engage authentically and amplify your leadership impact.
  </div>

  <h2 class="section-title offer-title">Analytic Coaching Group for Senior Leaders</h2>

  <div class="intro-card left">
    As a senior leader in healthcare, you’re constantly navigating challenges.<br>
    But where do you turn for authentic connections, reflection and personal growth?
  </div>
  <div class="intro-card right">
    Rethink your leadership assumptions and approach challenges with fresh creativity.<br>
    Secure your spot in our exclusive Analytic Coaching Group and ignite your leadership potential.
  </div>

  <h2 class="section-title benefits-title">Benefits to you</h2>
  <ul class="benefits">
    <li><svg width="16" height="12" viewBox="0 0 16 12"><path d="M1 6h12M9 2l4 4-4 4" stroke="#1d4a9a" stroke-width="2" fill="none"/></svg>Transformative conversations: Engage in discussions that spark innovative leadership</li>
    <li><svg width="16" height="12" viewBox="0 0 16 12"><path d="M1 6h12M9 2l4 4-4 4" stroke="#1d4a9a" stroke-width="2" fill="none"/></svg>Peer insights: Harness fresh insights from peers, enhancing your decision-making and effectiveness</li>
    <li><svg width="16" height="12" viewBox="0 0 16 12"><path d="M1 6h12M9 2l4 4-4 4" stroke="#1d4a9a" stroke-width="2" fill="none"/></svg>Reimagined leadership: Channel your creativity and redefine your leadership, personally and professionally</li>
    <li><svg width="16" height="12" viewBox="0 0 16 12"><path d="M1 6h12M9 2l4 4-4 4" stroke="#1d4a9a" stroke-width="2" fill="none"/></svg>Instant 360° insights: Gain real-time feedback from trusted peers to enrich your leadership</li>
    <li><svg width="16" height="12" viewBox="0 0 16 12"><path d="M1 6h12M9 2l4 4-4 4" stroke="#1d4a9a" stroke-width="2" fill="none"/></svg>Lead authentically: Develop effective strategies using the latest insights from group and leadership psychology</li>
  </ul>

  <blockquote class="quote-card">
    <p>“You bare your heart and share things you wouldn’t under normal circumstances. You get to know each other very quickly. There’s that sort of intense, shared experience that comes from speaking to each other’s lives.”</p>
    <cite>– Helen, Medical Director</cite>
  </blockquote>
  <span class="quote-mark open">“</span>
  <span class="quote-mark close">”</span>

  <div class="details">
    Dates: 7 February 2024 – 11 December 2024<br>
    Time: 7:30am - 8:45am (UK time).<br>
    Commitment: Wednesdays, every 2 weeks<br>
    Location: Connect from anywhere by Meetline<br>
    Cost: £3350 [UK] €3900 [Europe] A$6530 [Australia]<br>
    <span class="indent">Payment options available</span>
  </div>

  <div class="cta">
    Secure your spot now and<br>ignite your leadership potential..
  </div>
</main>
</body>
</html>
```